Redesign Website for Corvane Blaze

I have an existing website on https://www.corvaneblaze-demo.com.au/ and would like to have this redesigned professionally with new content (please refer to word document). We are fire protection engineers providing fire services design expertise and engineering design to a range of different clients.

We also provide drafting services to clients in the form of completing final commissioning documentation such as 'as-installed' drawings and fire services block plans to ensure compliance with the building code and relevant Australian Standards.

Target Market(s)

Builders, Architects, Consultants, Project Managers

Industry/Entity Type

Engineering Consultant

Coding

Coded - Design and coding required

Number of Pages Required

4 page

Font styles to use
Sans Serif

Requirements
Must have
• Home and about Page, fire services design page, fire block plans page, contact us page (4 Pages).

The website colour choice must match or compliment the new company logo.
Nice to have
• Quality photos of fire services installations in buildings to Australian Standards.

A website similar to this would be ideal http://quorbelflame-demo.com.au
Should not have
• Stolen licensed photos

```html
<!DOCTYPE html>
<html lang="en">
<head>
<meta charset="utf-8">
<title>Corvane Blaze — Fire Services</title>
<link href="https://fonts.googleapis.com/css2?family=Montserrat:wght@300;400;500;600;700&family=Oswald:wght@500&family=Roboto:wght@400;500&display=swap" rel="stylesheet">
<style>
:root{
  --orange:#f7931e;
  --orange-dark:#e8801a;
  --ink:#1b1b1b;
  --grey:#8c8c8c;
  --light:#f2f2f2;
  --peach:#fde9d4;
  --footer:#121212;
}
*{box-sizing:border-box;margin:0;padding:0}
html,body{width:1200px;height:4494px;overflow:hidden}
body{font-family:"Montserrat",sans-serif;color:var(--ink);background:#fff;position:relative}
.abs{position:absolute}
section,header,footer{position:absolute;left:0;width:1200px}

/* top bar */
.topbar{top:0;height:35px}
.topbar .band{position:absolute;left:620px;width:525px;height:35px;background:#111;display:flex;align-items:center;font-size:11px;color:#ddd}
.topbar .item{display:flex;align-items:center;gap:8px;padding:0 18px;height:35px}
.topbar .item + .item{border-left:1px solid #333}
.topbar b{color:#fff;font-weight:600}
.dot-ic{width:22px;height:22px;border-radius:50%;background:var(--orange);display:flex;align-items:center;justify-content:center}

/* nav */
.nav{top:35px;height:70px;border-bottom:1px solid #eee}
.brand{position:absolute;display:flex;align-items:center;gap:10px;font-weight:600;color:var(--orange);letter-spacing:.5px}
.nav .brand{left:58px;top:18px;font-size:17px}
.brand .mark{width:30px;height:30px;border-radius:50%;border:2px solid var(--orange)}
.menu{position:absolute;top:30px;left:0;font-size:11px;color:var(--grey);letter-spacing:.5px}
.menu span{position:absolute;white-space:nowrap}
.menu .on{color:var(--orange);font-weight:600}

/* hero */
.hero{top:105px;height:638px;background:radial-gradient(circle at 25% 45%,#7a3a34 0%,#3c2e2c 30%,#2b2d30 65%,#232528 100%)}
.hero .title{position:absolute;top:205px;width:100%;text-align:center;font-family:"Oswald",sans-serif;font-size:52px;color:#fff;letter-spacing:1px}
.hero p{position:absolute;top:286px;left:330px;width:540px;text-align:center;color:#eee;font-size:12.5px;line-height:22.5px}
.arrow-btn{position:absolute;top:380px;width:46px;height:46px;border-radius:50%;background:rgba(255,255,255,.25);display:flex;align-items:center;justify-content:center}
.pill{position:absolute;height:42px;border-radius:21px;background:var(--orange);color:#fff;font-size:12px;font-weight:500;display:flex;align-items:center;padding-left:18px;letter-spacing:.5px}
.pill i{position:absolute;right:3px;top:3px;width:36px;height:36px;border-radius:50%;background:#fff;opacity:.9;border:3px solid #ffd3a0}

/* generic section heads */
.h2{position:absolute;width:100%;text-align:center;font-weight:700;font-size:30px;letter-spacing:.5px}
.lead{position:absolute;left:0;right:0;margin:auto;text-align:center;color:var(--grey);font-size:11.5px;line-height:21px;font-weight:300}

/* fire block plans */
.plans{top:743px;height:957px}
.plan{position:absolute;width:240px;font-family:"Roboto",sans-serif}
.plan h3{font-size:15px;font-weight:500;margin-bottom:14px}
.plan p{font-family:"Montserrat",sans-serif;font-size:11px;color:var(--grey);line-height:20px;font-weight:300}
.plan .more{display:block;margin-top:16px;color:var(--orange);font-size:11px;font-family:"Montserrat",sans-serif;font-weight:500}
.plan.left{text-align:right}
.icon-hex{position:absolute;width:76px;height:76px}

/* about */
.about{top:1700px;height:790px;background:linear-gradient(#f7f7f7,#efefef)}
.about p{width:610px}
.photo-fit{position:absolute;left:0;top:358px;width:1200px;height:432px;background:linear-gradient(180deg,#f0f0f0 0%,#e6e6e6 40%,#c9ccd2 100%)}
.features{top:2490px;height:262px;display:flex}
.feature{height:262px;position:relative;color:#fff;text-align:center;font-size:13px;line-height:24px}
.feature p{position:absolute;top:140px;left:30px;right:30px}
.feature svg{position:absolute;top:55px;left:50%;margin-left:-32px}

/* drawings */
.drawings{top:2752px;height:945px}
.plan-frame{position:absolute;left:235px;top:225px;width:728px;height:389px;border:5px solid var(--orange);background:linear-gradient(135deg,#fafafa,#e9e9e9)}
.note{position:absolute;top:660px;width:100%;text-align:center;color:var(--orange);font-size:11.5px;line-height:20px}
.spec{position:absolute;font-size:11px;color:#555;line-height:20px;font-weight:400}
.spec li{list-style:none;position:relative;padding-left:28px;margin-bottom:10px}
.spec li::before{content:"";position:absolute;left:0;top:5px;width:11px;height:11px;background:var(--orange);clip-path:polygon(50% 0,100% 30%,100% 70%,50% 100%,0 70%,0 30%)}

/* contact */
.contact{top:3697px;height:450px}
.field{position:absolute;height:42px;border:1px solid #e3e3e3;font-size:10.5px;color:#999;padding:14px 14px}

/* footer */
.footer{top:4147px;height:347px;background:var(--footer);color:#ddd;font-size:11px}
.footer h4{position:absolute;top:76px;color:var(--orange);font-size:14px;font-weight:600}
.footer .col{position:absolute}
.footer ul li{list-style:none;height:26px;position:relative;padding-left:14px}
.footer ul li::before{content:"";position:absolute;left:0;top:6px;width:4px;height:4px;border-radius:50%;background:#ccc}
.gt{position:absolute;left:614px;display:flex;gap:14px;line-height:21px}
.gt .dot-ic{flex:none;margin-top:2px}
.social{position:absolute;top:120px;width:38px;height:38px;border-radius:50%}
</style>
</head>
<body>

<header class="topbar">
  <div class="band">
    <div class="item"><span class="dot-ic"><svg width="11" height="11" viewBox="0 0 24 24"><path fill="#fff" d="M6.6 10.8a15 15 0 0 0 6.6 6.6l2.2-2.2c.3-.3.7-.4 1-.2 1.1.4 2.3.6 3.6.6.6 0 1 .4 1 1V20c0 .6-.4 1-1 1A17 17 0 0 1 3 4c0-.6.4-1 1-1h3.5c.6 0 1 .4 1 1 0 1.3.2 2.5.6 3.6.1.3 0 .7-.2 1z"/></svg></span>Call Us : <b>+61 4 9051 2273</b></div>
    <div class="item"><span class="dot-ic"><svg width="11" height="11" viewBox="0 0 24 24"><path fill="#fff" d="M2 5h20v14H2z"/><path d="M2 5l10 8 10-8" stroke="#f7931e" stroke-width="2" fill="none"/></svg></span>Email Us : <b>info@corvaneblaze-demo.com.au</b></div>
  </div>
</header>

<header class="nav">
  <div class="brand"><span class="mark"></span>CORVANE BLAZE</div>
  <nav class="menu">
    <span class="on" style="left:563px">HOME</span>
    <span style="left:631px">ABOUT US</span>
    <span style="left:724px">FIRE SERVICES PLANS</span>
    <span style="left:877px">FIRE BLOCK PLANS</span>
    <span style="left:1016px">CONTACT US</span>
    <span style="left:1126px;top:-4px"><svg width="15" height="15" viewBox="0 0 24 24"><circle cx="10" cy="10" r="7" stroke="#f7931e" stroke-width="2.5" fill="none"/><path d="M15 15l6 6" stroke="#f7931e" stroke-width="2.5"/></svg></span>
  </nav>
  <svg class="abs" style="left:574px;top:49px" width="12" height="12"><circle cx="6" cy="6" r="4" stroke="#f7931e" stroke-width="1.5" fill="none"/></svg>
</header>

<section class="hero" role="img" aria-label="Photo of a red fire alarm call point mounted on a wall, darkened">
  <h1 class="title">CORVANE BLAZE FIRE SERVICES</h1>
  <p>We pride ourselves in our ability to meet the demand of our clients and our ability to consistently uphold our 3 key business values in providing our services at quick turnaround, quality service at competitive pricing</p>
  <a class="pill" style="left:525px;top:386px;width:148px">CONTACT US<i></i></a>
  <span class="arrow-btn" style="left:59px"><svg width="14" height="14" viewBox="0 0 24 24"><path d="M15 4l-8 8 8 8" stroke="#fff" stroke-width="2" fill="none"/></svg></span>
  <span class="arrow-btn" style="left:1093px"><svg width="14" height="14" viewBox="0 0 24 24"><path d="M9 4l8 8-8 8" stroke="#fff" stroke-width="2" fill="none"/></svg></span>
</section>

<section class="plans">
  <h2 class="h2" style="top:73px">FIRE BLOCK PLANS</h2>
  <p class="lead" style="top:131px;width:500px">We can can also assist you with the preparation of final commissioning documentation as required to achieve with relevant Australian Standards. Some of the services we provide (but not limited to) include</p>

  <svg class="abs" style="left:0;top:0" width="1200" height="957">
    <polygon points="403,417 500,239 696,239 794,417 696,595 500,595" fill="none" stroke="#fbd6ad" stroke-width="2"/>
    <polygon points="436,417 516,270 680,270 760,417 680,564 516,564" fill="#fde9d4"/>
    <g stroke="#fbd6ad" stroke-width="1.5">
      <line x1="397" y1="294" x2="456" y2="322"/><line x1="804" y1="294" x2="743" y2="322"/>
      <line x1="397" y1="519" x2="452" y2="497"/><line x1="804" y1="519" x2="745" y2="497"/>
      <line x1="598" y1="595" x2="598" y2="632"/>
    </g>
    <g fill="#f7931e" stroke="#fde0bf" stroke-width="4">
      <circle cx="456" cy="322" r="7"/><circle cx="743" cy="322" r="7"/>
      <circle cx="452" cy="497" r="7"/><circle cx="745" cy="497" r="7"/>
      <circle cx="598" cy="584" r="7"/>
    </g>
  </svg>
  <div class="abs" role="img" aria-label="Photo of a technician inspecting a wall-mounted fire extinguisher with a clipboard" style="left:467px;top:286px;width:265px;height:253px;clip-path:polygon(22% 0,78% 0,100% 50%,78% 100%,22% 100%,0 50%);background:linear-gradient(135deg,#e9eef2,#9fb0c0 45%,#c8402f 75%,#d9dde0)"></div>

  <!-- icon hexes -->
  <svg class="icon-hex" style="left:321px;top:256px" viewBox="0 0 76 76"><polygon points="19,4 57,4 74,38 57,72 19,72 2,38" fill="#fff" stroke="#eee" stroke-width="2"/><ellipse cx="38" cy="36" rx="16" ry="6" fill="none" stroke="#333" stroke-width="2"/><path d="M24 38q14 10 28 0" stroke="#f7931e" stroke-width="2" fill="none"/></svg>
  <svg class="icon-hex" style="left:321px;top:481px" viewBox="0 0 76 76"><polygon points="19,4 57,4 74,38 57,72 19,72 2,38" fill="#fff" stroke="#eee" stroke-width="2"/><rect x="28" y="20" width="20" height="36" rx="2" fill="none" stroke="#333" stroke-width="2"/><line x1="32" y1="27" x2="44" y2="27" stroke="#333" stroke-width="2"/><circle cx="38" cy="42" r="6" fill="none" stroke="#f7931e" stroke-width="2"/></svg>
  <svg class="icon-hex" style="left:804px;top:256px" viewBox="0 0 76 76"><polygon points="19,4 57,4 74,38 57,72 19,72 2,38" fill="#fff" stroke="#eee" stroke-width="2"/><rect x="26" y="22" width="24" height="6" fill="none" stroke="#333" stroke-width="2"/><path d="M38 28v6M30 40l-3 5M38 40v6M46 40l3 5" stroke="#f7931e" stroke-width="2"/></svg>
  <svg class="icon-hex" style="left:804px;top:481px" viewBox="0 0 76 76"><polygon points="19,4 57,4 74,38 57,72 19,72 2,38" fill="#fff" stroke="#eee" stroke-width="2"/><path d="M30 28h16v26H30zM26 34h24M26 48h24" fill="none" stroke="#333" stroke-width="2"/><circle cx="38" cy="40" r="4" fill="#f7931e"/></svg>
  <svg class="icon-hex" style="left:560px;top:632px" viewBox="0 0 76 76"><polygon points="19,4 57,4 74,38 57,72 19,72 2,38" fill="#fff" stroke="#eee" stroke-width="2"/><rect x="24" y="18" width="28" height="38" fill="none" stroke="#333" stroke-width="2"/><circle cx="40" cy="27" r="3" fill="#f7931e"/><path d="M39 31l-5 10 6 4-3 8M36 36l-6 3M41 36l6 2" stroke="#f7931e" stroke-width="2" fill="none"/></svg>

  <div class="plan left" style="left:51px;top:240px"><h3>Zone Block Plans</h3><p>AS1670.1 requires an automatic smoke detection and alarm system to incorporate a Zone Block Plan to be securely...</p><span class="more">LEARN MORE &nbsp;▶</span></div>
  <div class="plan left" style="left:51px;top:454px"><h3>EWIS / SSISEP Block Plans</h3><p>AS1670.4 requires an Emergency Warning and Intercom System (EWIS) / Sound System and Intercom System.</p><span class="more">LEARN MORE &nbsp;▶</span></div>
  <div class="plan" style="left:909px;top:240px"><h3>Sprinkler Block Plans</h3><p>AS2118.1 requires Automatic Fire Sprinkler Systems to incorporate a Sprinkler Block Plan to be located adjacent.</p><span class="more">LEARN MORE &nbsp;▶</span></div>
  <div class="plan" style="left:909px;top:454px"><h3>Fire Hydrant Block Plans</h3><p>AS2419.1 requires Fire Hydrant Systems to incorporate a Fire Hydrant Block Plan to be located at the location of fire.</p><span class="more">LEARN MORE &nbsp;▶</span></div>
  <div class="plan" style="left:468px;top:733px;width:264px;text-align:center"><h3 style="line-height:22px">Evacuation Management Plan / Diagrams</h3><p>AS3745 requires Evacuation Diagrams that provide emergency and evacuation information to be displayed.</p><span class="more">LEARN MORE &nbsp;▶</span></div>
</section>

<section class="about">
  <h2 class="h2" style="top:76px">ABOUT CORVANE BLAZE</h2>
  <p class="lead" style="top:134px">We pride ourselves in our ability to meet the demand of our clients and our ability to consistently uphold our 3 key business values in providing our services at quick turnaround, quality service at competitive pricing.</p>
  <p class="lead" style="top:195px">Corvane Blaze is a company based in Sydney, Australia providing the Australian market expertise in the field of fire safety. Our mission is to assist our clients with the preparation of design and specifications of fire services upgrades and final commissioning documentation to achieve compliance with the National Construction Code (NCC) and relevant Australian Standards.</p>
  <a class="pill" style="left:525px;top:311px;width:156px">LEARN MORE<i></i></a>
  <div class="photo-fit" role="img" aria-label="Photo of a technician installing a smoke detector on a white ceiling"></div>
</section>

<section class="features">
  <div class="feature" style="width:394px;background:linear-gradient(135deg,#f9a23a,#ef8c17)">
    <svg width="64" height="64" viewBox="0 0 64 64"><path d="M14 6h26l10 10v42H14z" fill="none" stroke="#fff" stroke-width="2.5"/><path d="M22 24h20M22 32h20M22 40h12" stroke="#fff" stroke-width="2.5"/><circle cx="46" cy="46" r="9" fill="#f39a2a" stroke="#fff" stroke-width="2.5"/><path d="M42 46l3 3 5-6" stroke="#fff" stroke-width="2.5" fill="none"/></svg>
    <p>We pride ourselves on our prompt service and delivery of all of our projects. You can rely on us to meet your project deadlines!</p>
  </div>
  <div class="feature" style="width:412px;background:linear-gradient(135deg,#2a2a2a,#1a1a1a)">
    <svg width="64" height="64" viewBox="0 0 64 64"><circle cx="32" cy="24" r="15" fill="none" stroke="#fff" stroke-width="2.5"/><circle cx="32" cy="24" r="8" fill="none" stroke="#fff" stroke-width="2"/><path d="M24 37l-6 20 8-4 4 7 2-12M40 37l6 20-8-4-4 7-2-12" fill="none" stroke="#fff" stroke-width="2.5"/></svg>
    <p>Our customer service and our output is guaranteed to be of the highest quality. You will not be disappointed.</p>
  </div>
  <div class="feature" style="width:394px;background:linear-gradient(135deg,#f9a23a,#ef8c17)">
    <svg width="64" height="64" viewBox="0 0 64 64"><path d="M8 34L34 8h20v20L28 54z" fill="none" stroke="#fff" stroke-width="2.5"/><circle cx="46" cy="16" r="3" fill="#fff"/><path d="M26 26v16M22 38c0 3 8 3 8-1s-8-3-8-7 8-3 8 0" stroke="#fff" stroke-width="2.5" fill="none"/></svg>
    <p>We strive to always be competitively priced are very competitively priced.</p>
  </div>
</section>

<section class="drawings">
  <h2 class="h2" style="top:75px">FIRE SERVICES DRAWINGS</h2>
  <p class="lead" style="top:130px;width:560px">Corvane Blaze can assist with the preparation of the design and specification for the upgrade or installation or new fire safety systems to achieve compliance with the National Construction Code (NCC), Council Fire Orders or Fire Engineering Reports</p>
  <div class="plan-frame" role="img" aria-label="Architectural floor plan drawing showing apartments, storage areas and a 35 metre hose coverage line"></div>
  <p class="note">We have proficient knowledge in the ability to produce design and specifications<br>relating to the below fire safety measures:</p>
  <ul class="spec" style="left:235px;top:724px;width:330px">
    <li>Automatic Smoke Detection and Alarm System</li>
    <li>Smoke Alarms</li>
    <li>Portable Fire Extinguishers</li>
    <li>Emergency Warning and Intercom System (EWIS) /Sound System and Intercom System for Emergency Purposes (SSISEP)</li>
  </ul>
  <ul class="spec" style="left:644px;top:724px;width:330px">
    <li>Occupant Warning System (OWS)</li>
    <li>Fire Hose Reels</li>
    <li>Fire Hydrant Systems</li>
    <li>Emergency Lighting and Exit signs</li>
  </ul>
</section>

<section class="contact">
  <h2 class="h2" style="top:46px">CONTACT US</h2>
  <p class="lead" style="top:104px;width:460px">Please send us your contact details below with project specific information and attachments; and we will get in touch with you immediately.</p>
  <div class="field" style="left:192px;top:182px;width:261px">Name :</div>
  <div class="field" style="left:469px;top:182px;width:262px">Email :</div>
  <div class="field" style="left:746px;top:182px;width:262px">Email :</div>
  <div class="field" style="left:192px;top:239px;width:816px;height:75px">Message / comments :</div>
  <a class="pill" style="left:521px;top:332px;width:158px;padding-left:20px">SUBMIT NOW<i></i></a>
</section>

<footer class="footer">
  <div class="brand" style="left:59px;top:110px;font-size:17px"><span class="mark"></span>CORVANE BLAZE</div>
  <p class="abs" style="left:59px;top:166px;width:220px;line-height:21px">We pride ourselves in our ability to meet the demand of our clients and our ability to consistently uphold our 3 key business values...<u>LEARN MORE</u></p>

  <h4 style="left:337px">LINKS</h4>
  <ul class="col" style="left:337px;top:118px">
    <li>Home</li><li>About Us</li><li>Fire Services Plans</li><li>Fire Block Plans</li><li>Contact Us</li>
  </ul>

  <h4 style="left:614px">GET IN TOUCH</h4>
  <div class="gt" style="top:118px"><span class="dot-ic"><svg width="10" height="12" viewBox="0 0 20 24"><path d="M10 0a8 8 0 0 0-8 8c0 6 8 16 8 16s8-10 8-16a8 8 0 0 0-8-8z" fill="#fff"/></svg></span><span>123,Address,Street Name, State<br>Name City Name, Zipcode.</span></div>
  <div class="gt" style="top:178px"><span class="dot-ic"><svg width="11" height="11" viewBox="0 0 24 24"><path fill="#fff" d="M6.6 10.8a15 15 0 0 0 6.6 6.6l2.2-2.2c.3-.3.7-.4 1-.2 1.1.4 2.3.6 3.6.6.6 0 1 .4 1 1V20c0 .6-.4 1-1 1A17 17 0 0 1 3 4c0-.6.4-1 1-1h3.5c.6 0 1 .4 1 1 0 1.3.2 2.5.6 3.6.1.3 0 .7-.2 1z"/></svg></span><span>ABN : 48 903 216 557<br>M : +61 4 9051 2274</span></div>
  <div class="gt" style="top:250px"><span class="dot-ic"><svg width="11" height="11" viewBox="0 0 24 24"><path fill="#fff" d="M2 5h20v14H2z"/><path d="M2 5l10 8 10-8" stroke="#f7931e" stroke-width="2" fill="none"/></svg></span><span>E : info@corvaneblaze-demo.com.au</span></div>

  <h4 style="left:888px">SOCIAL LINKS</h4>
  <span class="social" style="left:888px;background:#3b5b9a"></span>
  <span class="social" style="left:933px;background:#2a9fd6"></span>
  <span class="social" style="left:977px;background:#1c75b0"></span>
  <p class="abs" style="left:888px;top:180px;font-size:10px;color:#aaa;line-height:19px">Copyright © CORVANE BLAZE - 2021.<br>All right reserved.</p>
</footer>

</body>
</html>
```